Supplement Bottle Label Design and Creative Lifestyle Images

We are a medical home consumer brand and we are releasing a supplement line of products called "Velbrook Nutrition". We are in need of a supplement bottle design for our supplement line, Velbrook Nutrition. We are looking for a very appealing, simple, and clean design, but with a medical feel to it.

We would like to see designs with a black background as well as designs with a white background. Bottle size will approximately be 200cc and label will about be 7" x 2.5", but this size is subject to change.

We really like the Pirlen Nutrition design and the Gantry Lab, however, we like the medical style of Nutrition Keystones. Please reference the links below.

To start off, the title of this bottle will be "Calm-Spire". We will need all similar warning about FDA, made in USA, non-GMA, GMP, ect. Please use the formula below to start:

2 Pills per serving
Blueberry pterostilbene - 10mg
Bacopa - 150mg
Gingko Biloba - 50mg
Vinpocetine - 10mg
Alpha-GPC -150mg
TAU - 35mg

https://www.shopvarn.example/Pirlen-Nutrition/b/ref=bl_dp_s_web_48213907562?ie=UTF8&node=48213907562&field-lbr_brands_browse-bin=Pirlen+Nutrition

https://www.shopvarn.example/l/7394208156

https://www.shopvarn.example/Nutrition-Keystones/b/ref=bl_dp_s_web_86420531977?ie=UTF8&node=86420531977&field-lbr_brands_browse-bin=Nutrition+Keystones

Industry/Entity Type

Medical

```html
<!DOCTYPE html>
<html lang="en">
<head>
<meta charset="utf-8">
<title>Velbrook Nutrition – Calm-Spire Label</title>
<link rel="stylesheet" href="https://fonts.googleapis.com/css2?family=Nunito+Sans:wght@400;600;700;800;900&display=swap">
<style>
  :root {
    --label-black: #0c0c0d;
    --label-shade: #161618;
    --teal: #3cbfb7;
    --orange: #f5a11f;
    --white: #f3f3f3;
    --mint: #dcefed;
  }
  * { margin: 0; padding: 0; box-sizing: border-box; }
  html, body {
    width: 800px;
    height: 1200px;
    overflow: hidden;
    background: var(--label-black);
  }
  .label {
    position: relative;
    width: 800px;
    height: 1200px;
    background: var(--label-black);
    font-family: "Nunito Sans", sans-serif;
    color: var(--white);
    overflow: hidden;
  }
  .label-curves {
    position: absolute;
    inset: 0;
  }
  .brand {
    position: absolute;
    top: 150px;
    left: 0;
    width: 100%;
    text-align: center;
    font-weight: 800;
    font-size: 46px;
    letter-spacing: 0.5px;
    color: var(--white);
  }
  .brain-mark {
    position: absolute;
    top: 300px;
    left: 290px;
    width: 220px;
    height: 250px;
    border-radius: 48% 48% 40% 40%;
    background: radial-gradient(circle at 45% 40%, var(--mint) 0%, var(--teal) 55%, var(--orange) 100%);
    opacity: 0.85;
  }
  .seal {
    position: absolute;
    top: 390px;
    width: 96px;
    height: 96px;
    border-radius: 50%;
    border: 2px solid var(--teal);
  }
  .seal--left { left: 112px; }
  .seal--right { left: 592px; }
  .product-name {
    position: absolute;
    top: 580px;
    left: 0;
    width: 100%;
    text-align: center;
    font-weight: 800;
    font-size: 86px;
    letter-spacing: -1px;
    color: var(--teal);
  }
  .serving {
    position: absolute;
    top: 708px;
    left: 0;
    width: 100%;
    text-align: center;
    font-weight: 800;
    font-size: 15px;
    letter-spacing: 2.5px;
    color: var(--orange);
  }
  .formula {
    position: absolute;
    top: 760px;
    left: 0;
    width: 100%;
    list-style: none;
    text-align: center;
    font-weight: 600;
    font-size: 17px;
    line-height: 20.5px;
    color: var(--white);
  }
  .claims {
    position: absolute;
    top: 898px;
    left: 160px;
    width: 480px;
    padding: 8px 0;
    border-top: 1px solid var(--teal);
    border-bottom: 1px solid var(--teal);
    text-align: center;
    font-weight: 800;
    font-size: 11.5px;
    color: var(--teal);
  }
  .supplement-type {
    position: absolute;
    top: 981px;
    left: 0;
    width: 100%;
    text-align: center;
    font-weight: 800;
    font-size: 15px;
    letter-spacing: 2.5px;
    color: var(--orange);
  }
  .count {
    position: absolute;
    top: 1003px;
    left: 0;
    width: 100%;
    text-align: center;
    font-weight: 800;
    font-size: 15px;
    letter-spacing: 1.5px;
    color: var(--orange);
  }
</style>
</head>
<body>
  <main class="label">
    <svg class="label-curves" width="800" height="1200" viewBox="0 0 800 1200" aria-hidden="true">
      <path d="M0 860 C 180 760, 360 820, 520 1000 S 760 1200, 800 1200 L 0 1200 Z" fill="var(--label-shade)"/>
      <path d="M560 0 C 620 160, 800 260, 800 420 L 800 0 Z" fill="var(--label-shade)"/>
    </svg>

    <h1 class="brand">Velbrook Nutrition</h1>

    <div class="brain-mark" role="img" aria-label="Brain made of connected teal, orange and white molecule dots"></div>

    <div class="seal seal--left"></div>
    <div class="seal seal--right"></div>

    <h2 class="product-name">Calm-Spire</h2>

    <p class="serving">2 PILLS PER SERVING</p>

    <ul class="formula">
      <li>Blueberry pterostilbene | 10mg</li>
      <li>Bacopa | 50mg</li>
      <li>Gingko Biloba | 50mg</li>
      <li>Vinpocetine | 10mg</li>
      <li>Alpha-GPC | 150mg</li>
      <li>TAU | 35mg</li>
    </ul>

    <p class="claims">THIRD PARTY TESTED | FDA REGISTERED FACILITY | MADE IN THE USA</p>

    <p class="supplement-type">DIETARY SUPPLEMENT</p>
    <p class="count">200mg | 60 capsules</p>
  </main>
</body>
</html>
```